Trendy, rustic, patriotic Facebook Design!

Would like something to catch people's eye! Must include our logo and phone number. 410-587-3920. Dogs in the project are a must. Bold pricing, location, etc to catch peoples eyes is a plus.

Target Market(s)

Dog owners

Font styles to use
Serif
Sans Serif

Colors
1f66ae
ec1f27
ffffff

Requirements
Must have
• Dogs, company logo, business phone 410-587-3920 and website www.furlowpaws.com
Nice to have
• Something that is rustic, trendy!
Should not have
• Cartoons.

```html
<!DOCTYPE html>
<html lang="en">
<head>
<meta charset="UTF-8">
<title>Furlow Paws Dog Training – Free Consult</title>
<link rel="stylesheet" href="https://fonts.googleapis.com/css2?family=Arvo:wght@400;700&family=Barlow+Condensed:ital,wght@1,800&family=Open+Sans:wght@400&display=swap">
<style>
  :root {
    --navy: #0f2b5f;
    --navy-deep: #081a42;
    --navy-light: #15397a;
    --red: #b81c2e;
    --white: #ffffff;
    --grass-light: #7fb24a;
    --grass-dark: #4f8a2c;
  }
  * { margin: 0; padding: 0; box-sizing: border-box; }
  html, body { width: 1200px; height: 600px; overflow: hidden; background: var(--navy); }
  .banner {
    position: relative;
    width: 1200px;
    height: 600px;
    overflow: hidden;
    background:
      radial-gradient(ellipse at 70% 35%, var(--navy-light) 0%, transparent 60%),
      radial-gradient(ellipse at 15% 95%, var(--navy-deep) 0%, transparent 55%),
      var(--navy);
    color: var(--white);
  }
  .texture {
    position: absolute;
    inset: 0;
    width: 1200px;
    height: 600px;
    pointer-events: none;
  }
  .photo-frame {
    position: absolute;
    left: 32px;
    top: 34px;
    width: 410px;
    height: 531px;
    background: var(--red);
    padding: 10px;
  }
  .photo-frame__white {
    width: 100%;
    height: 100%;
    background: var(--white);
    padding: 10px;
  }
  .photo-frame__navy {
    width: 100%;
    height: 100%;
    background: var(--navy);
    padding: 7px;
  }
  .photo {
    width: 100%;
    height: 100%;
    background: linear-gradient(160deg, var(--grass-light) 0%, var(--grass-dark) 100%);
  }
  .brand {
    position: absolute;
    left: 615px;
    width: 400px;
    top: 86px;
    display: flex;
    flex-direction: column;
    align-items: center;
    font-family: "Arvo", serif;
    font-weight: 700;
    color: var(--white);
    line-height: 1;
  }
  .brand__mark {
    width: 64px;
    height: 64px;
    border: 4px solid var(--white);
    border-radius: 50%;
    margin-bottom: 16px;
  }
  .brand__name { font-size: 36px; letter-spacing: 1px; }
  .brand__tagline { font-size: 36px; letter-spacing: 1px; margin-top: 10px; }
  .headline {
    position: absolute;
    left: 500px;
    width: 630px;
    text-align: center;
    font-family: "Arvo", serif;
    font-weight: 400;
    color: var(--white);
    line-height: 1;
    -webkit-text-stroke: 0.8px var(--white);
  }
  .headline--top { top: 288px; font-size: 50px; }
  .headline--bottom { top: 368px; font-size: 48px; white-space: nowrap; }
  .headline__free {
    font-family: "Barlow Condensed", sans-serif;
    font-style: italic;
    font-weight: 800;
    font-size: 78px;
    vertical-align: -5px;
    margin: 0 6px;
    -webkit-text-stroke: 0;
  }
  .contact {
    position: absolute;
    top: 535px;
    left: 580px;
    display: flex;
    gap: 36px;
    font-family: "Open Sans", sans-serif;
    font-size: 22px;
    color: var(--white);
  }
  .contact__item { display: flex; align-items: center; gap: 6px; }
  .contact__icon { width: 30px; height: 30px; }
</style>
</head>
<body>
  <main class="banner">
    <svg class="texture" viewBox="0 0 1200 600" aria-hidden="true">
      <filter id="rustic-grain" x="0" y="0" width="100%" height="100%">
        <feTurbulence type="fractalNoise" baseFrequency="0.9" numOctaves="3" seed="4" result="grain"/>
        <feColorMatrix type="matrix" values="0 0 0 0 0.85  0 0 0 0 0.9  0 0 0 0 1  0 0 0 0.55 -0.18" in="grain"/>
      </filter>
      <filter id="rustic-mottle" x="0" y="0" width="100%" height="100%">
        <feTurbulence type="fractalNoise" baseFrequency="0.012" numOctaves="4" seed="9" result="mottle"/>
        <feColorMatrix type="matrix" values="0 0 0 0 0.02  0 0 0 0 0.06  0 0 0 0 0.2  0 0 0 1.1 -0.45" in="mottle"/>
      </filter>
      <rect width="1200" height="600" filter="url(#rustic-mottle)"/>
      <rect width="1200" height="600" filter="url(#rustic-grain)" opacity="0.35"/>
    </svg>

    <div class="photo-frame">
      <div class="photo-frame__white">
        <div class="photo-frame__navy">
          <div class="photo" role="img" aria-label="Photo of two happy dogs lying on green grass"></div>
        </div>
      </div>
    </div>

    <div class="brand">
      <div class="brand__mark" aria-hidden="true"></div>
      <div class="brand__name">FURLOW PAWS</div>
      <div class="brand__tagline">DOG TRAINING</div>
    </div>

    <h1 class="headline headline--top">CONTACT US</h1>
    <p class="headline headline--bottom">FOR A <span class="headline__free">FREE</span> CONSULT</p>

    <div class="contact">
      <div class="contact__item">
        <svg class="contact__icon" viewBox="0 0 30 30" aria-hidden="true">
          <circle cx="15" cy="15" r="13" fill="none" stroke="#fff" stroke-width="2"/>
          <rect x="11" y="7.5" width="8" height="15" rx="1.5" fill="none" stroke="#fff" stroke-width="1.8" transform="rotate(25 15 15)"/>
          <circle cx="15" cy="19.5" r="1" fill="#fff" transform="rotate(25 15 15)"/>
        </svg>
        <span>410-587-3920</span>
      </div>
      <div class="contact__item">
        <svg class="contact__icon" viewBox="0 0 30 30" aria-hidden="true">
          <circle cx="15" cy="15" r="13" fill="none" stroke="#fff" stroke-width="2"/>
          <g fill="none" stroke="#fff" stroke-width="1.4">
            <circle cx="15" cy="15" r="8"/>
            <ellipse cx="15" cy="15" rx="3.5" ry="8"/>
            <line x1="7" y1="15" x2="23" y2="15"/>
            <line x1="8.5" y1="11" x2="21.5" y2="11"/>
            <line x1="8.5" y1="19" x2="21.5" y2="19"/>
          </g>
        </svg>
        <span>www.furlowpaws.com</span>
      </div>
    </div>
  </main>
</body>
</html>
```